New Business Card Design for a Payroll Concierge Company

I need a new business card design that is simple and includes my current information. I am a payroll concierge company that processes payroll for clients who employ household employees and I also manage my client's personal bills, financial records. I want to include my current logo and a logo for an association (PFHKT) I belong too on the front of my business card. I will include both my all my company logo files and the association logo files.

Target Market(s)

People who hire household employees, nannies, home health aides, butlers, maids, etc for wealthy individuals and senior citizens who need help in the home.

Industry/Entity Type

Financial Service

Contact Information for Business Card

Company logo

Name: Martin L. Vellacourt
Managing Director

Office number: 555-555-0148
Business Cell: 555-555-0173

Website: www.tallywagedesk.net
Email: Martin.Vellacourt@tallywagedesk.com

Company address:

17 Heron Lane
Suite 208
Quillbrook,QB 06412

Font styles to use
Serif
Sans Serif

Colors
3176b5
85cae6
cee9f5
33a6d7
d3d3d3
dbdbdb

Requirements
Must have
• I need to have my company logo and name, phone numbers, website, email, and address on the card. I also want the association logo on the card somewhere but not too big. Small enough to see the logo maybe on the top or bottom corner. Or some where on there card that it doesn't take away the design.
Nice to have
• i like the blue color in my logo, grey, please see must haves business card details.
Should not have
• PLEASE DO NOT USE THE BUSINESS CARD DESIGNS IN THE FILES I UPLOADED. I AM NOT INTERESTED IN THAT DESIGN. ALSO THE ADDRESS AND WEBSITE ARE INCORRECT ON THOSE DESIGNS. PLEASE USE THE UPDATED INFO ON BUSINESS CARD DETAILS

```html
<!DOCTYPE html>
<html lang="en">
<head>
<meta charset="utf-8">
<title>Tallywage Desk – Business Card</title>
<link href="https://fonts.googleapis.com/css2?family=Montserrat:wght@600;700&family=Open+Sans:ital,wght@0,400;0,700;1,400&display=swap" rel="stylesheet">
<style>
  :root {
    --brand-blue: #3176b5;
    --sky-blue: #33a6d7;
    --mist-blue: #85cae6;
    --ice-blue: #cee9f5;
    --paper: #ffffff;
    --backdrop: #d3d3d3;
    --backdrop-light: #dbdbdb;
    --ink-light: #ffffff;
    --ink-soft: #d6e6f4;
    --badge-navy: #1d3f7a;
  }
  * { box-sizing: border-box; margin: 0; padding: 0; }
  html, body { width: 1200px; height: 960px; overflow: hidden; }
  body {
    background: radial-gradient(circle at 50% 40%, var(--backdrop-light), var(--backdrop));
    font-family: "Open Sans", Arial, sans-serif;
    position: relative;
  }
  .card {
    position: absolute;
    left: 220px;
    width: 760px;
    height: 432px;
    overflow: hidden;
    box-shadow: 0 6px 18px rgba(0,0,0,0.18);
  }
  .card--front { top: 28px; background: var(--paper); }
  .card--back  { top: 500px; background: var(--brand-blue); }

  /* front bands */
  .band { position: absolute; display: flex; width: 100%; height: 26px; }
  .band--top { top: 0; }
  .band--bottom { bottom: 0; }
  .band span { height: 100%; }
  .band--top .seg-main  { width: 78.5%; background: var(--brand-blue); }
  .band--top .seg-sky   { width: 11.8%; background: var(--sky-blue); }
  .band--top .seg-mist  { flex: 1; background: var(--mist-blue); }
  .band--bottom .seg-mist { width: 9.5%; background: var(--mist-blue); }
  .band--bottom .seg-sky  { width: 11.8%; background: var(--sky-blue); }
  .band--bottom .seg-main { flex: 1; background: var(--brand-blue); }

  .front-brand {
    position: absolute;
    left: 0; right: 0; top: 50%;
    transform: translateY(-50%);
    display: flex; align-items: center; justify-content: center; gap: 16px;
  }
  .brand-mark { width: 30px; height: 30px; background: var(--brand-blue); }
  .brand-name {
    font-family: "Montserrat", Arial, sans-serif;
    font-weight: 700;
    font-size: 38px;
    color: var(--brand-blue);
    letter-spacing: 1px;
    text-transform: uppercase;
  }

  /* back stripes */
  .stripe { position: absolute; top: 0; bottom: 0; }
  .stripe--ice  { left: 58.6%; width: 9.5%; background: var(--ice-blue); }
  .stripe--mist { left: 68.1%; width: 12%; background: var(--mist-blue); }
  .stripe--sky  { left: 80.1%; right: 0; background: var(--sky-blue); }

  .back-brand {
    position: absolute; left: 36px; top: 42px;
    display: flex; align-items: center; gap: 8px;
  }
  .back-brand .brand-mark { width: 14px; height: 14px; background: var(--ink-light); }
  .back-brand .brand-name { font-size: 16px; color: var(--ink-light); letter-spacing: 0.5px; }

  .contact { position: absolute; left: 36px; top: 124px; color: var(--ink-light); }
  .person-name {
    font-family: "Montserrat", Arial, sans-serif;
    font-weight: 700;
    font-size: 25px;
    letter-spacing: 0.5px;
    text-transform: uppercase;
  }
  .person-title {
    font-style: italic; font-size: 13px; color: var(--ink-soft);
    text-transform: uppercase; margin-top: 2px;
  }
  .address { margin-top: 46px; font-size: 17px; line-height: 22px; }
  .lines { margin-top: 46px; font-size: 17px; line-height: 22px; }
  .website { font-weight: 700; }

  .association-badge {
    position: absolute; right: 22px; bottom: 28px;
    width: 112px; height: 34px;
  }
</style>
</head>
<body>
  <section class="card card--front" aria-label="Business card front">
    <div class="band band--top"><span class="seg-main"></span><span class="seg-sky"></span><span class="seg-mist"></span></div>
    <div class="front-brand">
      <span class="brand-mark"></span>
      <span class="brand-name">Tallywage Desk</span>
    </div>
    <div class="band band--bottom"><span class="seg-mist"></span><span class="seg-sky"></span><span class="seg-main"></span></div>
  </section>

  <section class="card card--back" aria-label="Business card back">
    <div class="stripe stripe--ice"></div>
    <div class="stripe stripe--mist"></div>
    <div class="stripe stripe--sky"></div>

    <div class="back-brand">
      <span class="brand-mark"></span>
      <span class="brand-name">Tallywage Desk</span>
    </div>

    <div class="contact">
      <h1 class="person-name">Martin L. Vellacourt</h1>
      <p class="person-title">Managing Director</p>
      <p class="address">17 Heron Lane<br>Suite 208<br>Quillbrook,QB 06412</p>
      <p class="lines">
        Office: 555-555-0148<br>
        Business: 555-555-0173<br>
        Email: Martin.Vellacourt@tallywagedesk.com<br>
        <span class="website">www.tallywagedesk.net</span>
      </p>
    </div>

    <svg class="association-badge" viewBox="0 0 112 34" role="img" aria-label="PFHKT association member badge">
      <rect x="0" y="0" width="112" height="34" rx="3" fill="var(--badge-navy)"/>
    </svg>
  </section>
</body>
</html>
```